Brand refresh of quote, work docket and Fire certificate documents

I would like a refresh of our document suit including

1. Front page called VANTO3 Proposal
2. Quote document template
3. Work docket template
4. Fire certificate template - to look like a professional complaint certificate

Examples of documents are attached.

```html
<!DOCTYPE html>
<html lang="en">
<head>
<meta charset="utf-8">
<title>VANTO3 Document Suite</title>
<link rel="stylesheet" href="https://fonts.googleapis.com/css2?family=Open+Sans:ital,wght@0,400;0,600;0,700;1,400&family=Russo+One&display=swap">
<style>
:root{
  --red:#cc2230;
  --ink:#3a3a3c;
  --text:#2b2b2b;
  --grey-bg:#b3b4b6;
  --paper:#ffffff;
  --faint-text:#d2d2d4;
  --wash-warm:#fbe1dc;
  --wash-grey:#e8e8e9;
  --flame-wash:#fde9e2;
}
*{box-sizing:border-box;margin:0;padding:0}
html,body{width:1200px;height:1200px;overflow:hidden;background:var(--grey-bg)}
body{position:relative;font-family:"Open Sans",Arial,sans-serif;color:var(--text)}
.page{position:absolute;width:577px;height:816px;background:var(--paper);transform:scale(0.625);transform-origin:0 0;overflow:hidden}
.p1{left:230px;top:78px}
.p2{left:617px;top:78px}
.p3{left:230px;top:619px}
.p4{left:617px;top:619px}
.abs{position:absolute}
.footer{position:absolute;left:0;bottom:0;width:100%;height:41px;background:var(--red);color:#fff;font-weight:700;font-size:15px;text-align:center;line-height:41px;letter-spacing:.3px}
.divider{position:absolute;left:419px;top:0;width:1.5px;background:var(--red)}
.contact{position:absolute;left:430px;font-size:9.5px;line-height:13.5px;color:var(--text)}
.contact .co{color:var(--red);font-weight:700}
.contact b{font-weight:700}
.mail{display:inline-block;width:10px;height:7px;background:var(--red);margin-right:4px;vertical-align:middle}
.brand .name{font-weight:700;color:var(--ink);letter-spacing:-1px;line-height:1;display:flex;align-items:center}
.brand .name i{display:inline-block;background:var(--red);margin-left:6px}
.brand .tag{font-size:9px;letter-spacing:4px;color:var(--ink);margin-top:4px}
.wash-panel{position:absolute;left:412px;top:258px;width:133px;height:487px;border-radius:12px;
  background:linear-gradient(180deg,var(--wash-warm) 0%,#fdf0ec 26%,var(--wash-grey) 30%,var(--wash-grey) 100%);opacity:.75}
.deco-tag{position:absolute;left:551px;top:255px;height:495px;writing-mode:vertical-rl;transform:rotate(180deg);font-size:19px;letter-spacing:9.6px;color:var(--faint-text);text-align:center}
.flame-wash{position:absolute;width:66px;height:40px;border-radius:8px;background:linear-gradient(90deg,rgba(253,233,226,0) 0%,var(--flame-wash) 45%,rgba(253,233,226,0) 100%)}
.red{color:var(--red)}
.doc-title{position:absolute;font-family:"Russo One",sans-serif;color:var(--red);letter-spacing:.5px}
.body{font-size:10px;line-height:14px}
.body b{font-weight:700}
.item{margin-bottom:15px;position:relative}
.item .n{position:absolute;right:0;color:var(--red)}
</style>
</head>
<body>

<section class="page p1">
  <div class="wash-panel" role="img" aria-label="Faint brand wash"></div>
  <div class="deco-tag">PASSIVE FIRE PROTECTION</div>
  <div class="brand abs" style="left:38px;top:70px">
    <div class="name" style="font-size:58px">VANTO3<i style="width:14px;height:14px"></i></div>
    <div class="tag">PASSIVE FIRE PROTECTION</div>
  </div>
  <div class="divider" style="height:145px"></div>
  <div class="contact" style="top:74px">
    <div class="co">VANTO3 Pty Ltd</div>
    <div>4/22 Larkmoor Street</div>
    <div>Bayfield VIC 3185</div>
    <div style="margin-top:2px"><b>ABN:</b> 48 602 915 314</div>
    <div style="margin-top:2px"><span class="mail"></span>admin@vanto3.com.au</div>
  </div>

  <div class="abs" style="left:38px;top:185px;font-weight:700;font-size:54px;line-height:56px;color:var(--red)">VANTO3</div>
  <div class="abs" style="left:38px;top:243px;font-weight:700;font-size:54px;line-height:60px;color:var(--ink)">PROPOSAl</div>
  <div class="abs" style="left:40px;top:306px;width:291px;height:3px;background:var(--red)"></div>

  <svg class="abs" style="left:41px;top:334px" width="14" height="13" viewBox="0 0 14 13"><rect x="1" y="2" width="12" height="10" rx="1" fill="none" stroke="#cc2230" stroke-width="1.4"/><rect x="1" y="2" width="12" height="3" fill="#cc2230"/><g fill="#cc2230"><rect x="3" y="7" width="2" height="1.5"/><rect x="6" y="7" width="2" height="1.5"/><rect x="9" y="7" width="2" height="1.5"/><rect x="3" y="9.5" width="2" height="1.5"/><rect x="6" y="9.5" width="2" height="1.5"/></g></svg>
  <div class="abs" style="left:63px;top:331px;font-size:13px;font-weight:700">26th October, 2023</div>

  <div class="abs" style="left:41px;top:370px;font-size:13px;line-height:19px">
    <div class="red" style="font-weight:600">PREPARED FOR</div>
    <div style="font-weight:700">Norvale Builders</div>
    <div>71 Trevor St</div>
    <div>Port Arlen VIC 3211</div>
    <div>Marcello</div>
  </div>

  <svg class="abs" style="left:42px;top:495px" width="11" height="15" viewBox="0 0 11 15"><path d="M5.5 0C2.5 0 0 2.4 0 5.4 0 9.4 5.5 15 5.5 15S11 9.4 11 5.4C11 2.4 8.5 0 5.5 0Z" fill="#cc2230"/><circle cx="5.5" cy="5.4" r="2" fill="#fff"/></svg>
  <div class="abs" style="left:64px;top:484px;font-size:13px;line-height:19px">
    <div class="red" style="font-weight:600">PROJECT/WORKS LOCATION</div>
    <div style="font-weight:700">14 Orwin Street, Ashgrove Park</div>
  </div>

  <svg class="abs" style="left:41px;top:551px" width="13" height="13" viewBox="0 0 13 13"><rect x="1" y="1" width="8" height="11" fill="none" stroke="#cc2230" stroke-width="1.2"/><path d="M3 4h4M3 6.5h4M3 9h2" stroke="#cc2230" stroke-width="1"/><path d="M7 10l5-5" stroke="#cc2230" stroke-width="1.6"/></svg>
  <div class="abs" style="left:64px;top:541px;font-size:13px;line-height:19px">
    <div class="red" style="font-weight:600">PROPOSAL NO</div>
    <div style="font-weight:700">1188</div>
  </div>

  <div class="abs" role="img" aria-label="City skyline at dusk" style="left:0;top:592px;width:335px;height:183px;background:linear-gradient(180deg,#2c4ea8 0%,#3c62b8 40%,#5a5f86 70%,#3b3038 100%)"></div>
  <div class="flame-wash" role="img" aria-label="Faint flame motif" style="left:336px;top:607px"></div>

  <div class="footer">www.vanto3.com.au</div>
</section>

<section class="page p2">
  <div class="wash-panel" role="img" aria-label="Faint brand wash"></div>
  <div class="deco-tag">PASSIVE FIRE PROTECTION</div>
  <div class="brand abs" style="left:40px;top:55px">
    <div class="name" style="font-size:38px">VANTO3<i style="width:10px;height:10px"></i></div>
    <div class="tag" style="font-size:6.5px;letter-spacing:3px">PASSIVE FIRE PROTECTION</div>
  </div>
  <div class="divider" style="height:115px"></div>
  <div class="contact" style="top:32px">
    <div class="co">VANTO3 Pty Ltd</div>
    <div>4/22 Larkmoor Street</div>
    <div>Bayfield VIC 3185</div>
    <div style="margin-top:2px"><b>ABN:</b> 48 602 915 314</div>
    <div style="margin-top:2px"><span class="mail"></span>admin@vanto3.com.au</div>
  </div>
  <div class="doc-title" style="left:430px;top:110px;font-size:27px">QUOTE</div>

  <div class="abs" style="left:40px;top:165px;font-size:12.5px;line-height:19px">
    <div class="red" style="font-weight:600">1st May, 2025</div>
    <div>Quote Number: <span class="red">2196</span></div>
  </div>
  <div class="abs body" style="left:40px;top:216px;width:495px">
    <div>TO</div>
    <div><b>Sentry Check</b></div>
    <div>Daniel Hollis</div>
    <p style="margin-top:14px">Thank you for allowing us to provide a quotation for the fire resistant sealing of your service penetration requirements. Works to be completed as per site inspection at <b>88 Calder Street, West Brenton</b> listed below.</p>
    <p class="red" style="margin:14px 0;font-style:italic">*As per Keystone Compliance Inspection Report # 24232 provided.</p>
    <div class="item"><b>Basement – Stairwell to Carpark</b><br>1 x 20mm penetration with conduit through slab wall (one side only)<span class="n" style="top:14px">(1)</span></div>
    <div class="item"><b>Basement – Stairwell</b><br>Excluded as per report (separate price can be provided)<span class="n" style="top:14px">(2)</span></div>
    <div class="item"><b>Basement – Stairwell to Carpark</b><br>1 x 20mm penetration with conduit through plaster wall (one side only)<span class="n" style="top:14px">(3)</span></div>
    <div class="item"><b>Basement – Front External EV Carpark</b><br>1 x 100mm penetration with floor waste PVC pipe through slab roof<br>Excluded as per report (separate price can be provided)<span class="n" style="top:14px">(4)</span><span class="n" style="top:28px">(5)</span></div>
    <div class="item"><b>Basement – Carpark 3-08</b><br>1 x 40mm penetration with PVC pipe (fireboard plate &amp; collar required) through slab roof<span class="n" style="top:14px">(6)</span></div>
    <div class="item"><b>Ground Floor – Electrical Cupboard Next to G10</b><br>8 x 30mm x 30mm penetration with cables through plaster wall (one side only)<span class="n" style="top:14px">(7)</span></div>
    <div class="item"><b>Level 2 – Hydraulic Riser Opposite 213</b><br>2 x 50mm penetration with copper pipe &amp; wrap (refix) through plaster wall (one side only)<span class="n" style="top:14px">(8)</span></div>
    <div class="item"><b>Level 2 – Electrical Cupboard Next to 203</b><br>1 x 150mm x 150mm penetration with cables through plaster wall (one side only)<br>1 x 20mm penetration with conduit through plaster wall (one side only)<span class="n" style="top:14px">(9)</span><span class="n" style="top:28px">(10)</span></div>
    <div class="item"><b>Level 2 – Electrical Cupboard Next to 204</b><br>3 x 150mm x 100mm penetration with cables through plaster wall (one sideonly)<span class="n" style="top:14px">(11)</span></div>
  </div>
  <div class="footer">www.vanto3.com.au</div>
</section>

<section class="page p3">
  <div class="wash-panel" role="img" aria-label="Faint brand wash"></div>
  <div class="deco-tag">PASSIVE FIRE PROTECTION</div>
  <div class="flame-wash" role="img" aria-label="Faint flame motif" style="left:333px;top:612px"></div>
  <div class="brand abs" style="left:40px;top:55px">
    <div class="name" style="font-size:38px">VANTO3<i style="width:10px;height:10px"></i></div>
    <div class="tag" style="font-size:6.5px;letter-spacing:3px">PASSIVE FIRE PROTECTION</div>
  </div>
  <div class="divider" style="height:115px"></div>
  <div class="contact" style="top:32px">
    <div class="co">VANTO3 Pty Ltd</div>
    <div>4/22 Larkmoor Street</div>
    <div>Bayfield VIC 3185</div>
    <div style="margin-top:2px"><b>ABN:</b> 48 602 915 314</div>
    <div style="margin-top:2px"><span class="mail"></span>admin@vanto3.com.au</div>
  </div>
  <div class="doc-title" style="right:40px;top:110px;font-size:27px">WORK DOCKET</div>

  <div class="abs" style="left:41px;top:165px;font-size:12.5px;line-height:19px">
    <div class="red" style="font-weight:600">1st May, 2025</div>
    <div>Work Docket: 1190</div>
  </div>
  <div class="abs body" style="left:41px;top:222px;width:370px">
    <div><b>Harlow (VIC) Pty Ltd</b></div>
    <div>29 Marden Road</div>
    <div>Elwick West, VIC 3084</div>
    <div><b>Ryan Castell</b></div>
    <p style="margin-top:28px;width:360px">Works completed at SYD04 – 417 Birch Road, Tallowvale as directed by Ryan Castell of Harlow (VIC) Pty Ltd as listed below.</p>
    <p class="red" style="margin:14px 0">*Extra works – smoke wall to fire wall</p>
    <div class="item" style="margin-bottom:14px"><b>Ground Floor – MMR 2 Room</b><br>1 x 700mm x 400mm penetration with cable tray through plaster wall<br>1 x 400mm x 400mm penetration with cables through plaster wall<br>1 x 300mm x 150mm penetration with cable tray through plaster wall<br>1 x 700mm x 200mm penetration with cable tray through plaster wall<br>1 x 700mm x 200mm penetration with cable tray (Kelso) through plaster wall</div>
    <div class="item" style="margin-bottom:14px"><b>Ground Floor – FCR Room</b><br>1 x 600mm x 200mm penetration with cable tray through plaster wall<br>1 x 250mm x 250mm penetration with cables through plaster wall<br>1 x 400mm x 300mm penetration with cable tray through plaster wall</div>
    <div class="item" style="margin-bottom:14px"><b>Labour</b><br>02/11/23 1 Man x 10hrs = 10hrs $1250.00<br>03/11/23 1 Man x 8hrs = 8hrs $1000.00<br>09/11/23 1 Man x 4hrs = 4hrs $500.00</div>
    <div class="item" style="margin-bottom:14px"><b>Materials</b><br>2 x Rod bundle $100.00<br>2 x Fire Rated Batts $280.00<br>20 x Caulk (Ltr) $500.00<br>10 x HPE 300ml (Kelso) 300.00<br>1 x Flexwrap 40 (Roll) $250.00<br>40 x Fire Bricks (Kelso) $2000.00<br>3 x Fire Bandage (Kelso) $300.00</div>
    <div><b>Price for Labour &amp; Materials - TOTAL: $6,480 + GST</b></div>
  </div>
  <div class="footer">www.vanto3.com.au</div>
</section>

<section class="page p4">
  <div class="wash-panel" role="img" aria-label="Faint brand wash"></div>
  <div class="deco-tag">PASSIVE FIRE PROTECTION</div>
  <div class="flame-wash" role="img" aria-label="Faint flame motif" style="left:328px;top:607px"></div>
  <div class="abs" style="left:25px;top:26px;width:527px;height:723px;border:4px solid var(--red)"></div>
  <div class="brand abs" style="left:46px;top:72px">
    <div class="name" style="font-size:38px">VANTO3<i style="width:10px;height:10px"></i></div>
    <div class="tag" style="font-size:6.5px;letter-spacing:3px">PASSIVE FIRE PROTECTION</div>
  </div>
  <div class="divider" style="top:30px;height:90px"></div>
  <div class="contact" style="top:48px">
    <div class="co">VANTO3 Pty Ltd</div>
    <div>4/22 Larkmoor Street</div>
    <div>Bayfield VIC 3185</div>
    <div style="margin-top:2px"><b>ABN:</b> 48 602 915 314</div>
    <div style="margin-top:2px"><span class="mail"></span>admin@vanto3.com.au</div>
  </div>
  <div class="doc-title" style="left:84px;top:187px;font-size:22px">FIRE/SMOKE SYSTEM CERTIFICATE</div>

  <div class="abs body" style="left:85px;top:288px;width:305px">
    <div><b style="display:inline-block;width:70px">Client</b>: <b>Sentry Check Pty Ltd</b></div>
    <div style="margin-top:3px"><b style="display:inline-block;width:70px">Job</b>: <b>502 Bellmont Road, Hawkridge</b></div>
    <div style="margin-top:3px"><b>Certificate Number: 2324</b></div>
    <div style="margin-top:3px;display:flex"><b style="width:70px;flex:none">Reference</b><span style="flex:none;margin-right:6px">:</span><span>Fire/smoke sealing of your various service penetrations as detailed below.</span></div>
    <p style="margin-top:18px">VANTO3 Pty. Ltd. certifies that as part of our contracted works, we have carried out the above fire protection at 502 Bellmont Road, Hawkridge as instructed by Lena Vo of Sentry Check Pty Ltd.</p>
    <p style="margin-top:14px">These works have been completed and checked using the approved proprietary fire resistance tested products &amp; systems as per AS1530 part 4 &amp; AS4072 part 1</p>
    <p style="margin-top:14px">Any works that are modified, damaged, or disturbed following completion are not covered by this certification.</p>
    <p style="margin-top:14px">Installed in accordance with the manufacturer’s specifications.</p>
    <div style="margin-top:24px;display:flex;align-items:center"><b style="width:50px">Signed :</b><span role="img" aria-label="Handwritten signature" style="display:inline-block;width:75px;height:12px;background:linear-gradient(90deg,#cfcfd1,#e6e6e8)"></span></div>
    <div style="margin-top:22px"><b style="display:inline-block;width:50px">Name :</b>Tomas Keller</div>
    <div style="margin-top:14px"><b style="display:inline-block;width:50px">Date :</b>28th May, 2026</div>
  </div>
  <div class="footer">www.vanto3.com.au</div>
</section>

</body>
</html>
```